Buchcover-Design für Science-Fiction-Roman
Besonders gut hat mir die Eigeninitiative, Kreativität und Schnelligkeit gefallen. Vielen Dank für die tolle Zusammenarbeit.
Zielgruppe
Ich habe einen Science-Fiction-Roman geschrieben und benötige dafür ein Buchcover.
Meine Zielgruppe sind Leser- und Leserinnen ab 18, Science-Fiction-Fans.
Aufgabenstellung
Zur Einstimmung und Orientierung habe ich ein kurzes Exposé und eine Leseprobe des Romans hochgeladen.
Für das Cover stelle ich mir etwas Dezentes aber trotzdem künstlerisch Anspruchsvolles vor, gerne auch abstrakt.
Es sollte der Titel (Am Rande), meine Name (Lorenz Vadek) und 'Roman' auf dem Cover.
Den genauen Klappentext reiche ich noch nach.
Das Format ist 12,7 x 20,32 cm (5 x 8 Zoll), Rückenbreite etwa 2 cm.

```html
<!DOCTYPE html>
<html lang="de">
<head>
<meta charset="utf-8">
<title>Am Rande – Lorenz Vadek</title>
<link rel="stylesheet" href="https://fonts.googleapis.com/css2?family=Montserrat:wght@700;800&display=swap">
<style>
  :root {
    --page: #ecebe9;
    --sky-light: #dde9f0;
    --sky-mid: #c4dce8;
    --grid-line: #1d2e3d;
    --ink: #14181d;
    --title-panel: rgba(235, 243, 248, 0.75);
    --photo-dark: #0c0f12;
    --photo-soft: #3a4650;
  }
  * { margin: 0; padding: 0; box-sizing: border-box; }
  html, body {
    width: 1200px; height: 1200px; overflow: hidden;
    background: var(--page);
  }
  .book-cover {
    position: absolute;
    left: 281px; top: 55px;
    width: 680px; height: 1091px;
    background: linear-gradient(160deg, var(--sky-light) 0%, var(--sky-mid) 45%, var(--sky-light) 100%);
    overflow: hidden;
  }
  .cover-art {
    position: absolute; inset: 0;
    width: 100%; height: 100%;
  }
  .stacked-letters {
    position: absolute;
    display: flex; flex-direction: column; align-items: center;
    font-family: 'Montserrat', sans-serif;
    color: var(--ink);
    line-height: 1;
  }
  .stacked-letters span { display: block; }
  .title-panel {
    position: absolute;
    left: 313px; top: 260px;
    width: 51px; height: 458px;
    background: var(--title-panel);
  }
  .book-title {
    left: 313px; width: 51px; top: 279px;
    font-size: 26px; font-weight: 800;
  }
  .book-title span { height: 49px; }
  .author-name {
    left: 33px; width: 30px; top: 332px;
    font-size: 16px; font-weight: 800;
  }
  .author-name span { height: 32.4px; }
  .genre-label {
    left: 33px; width: 30px; top: 770px;
    font-size: 11px; font-weight: 700;
  }
  .genre-label span { height: 20px; }
</style>
</head>
<body>
  <div class="book-cover">
    <svg class="cover-art" viewBox="0 0 623 1000" preserveAspectRatio="none" xmlns="http://www.w3.org/2000/svg">
      <defs>
        <linearGradient id="lane-shade" x1="0" y1="0" x2="0" y2="1">
          <stop offset="0" stop-color="#b2d0e1"/>
          <stop offset="1" stop-color="#d2e3ec"/>
        </linearGradient>
        <linearGradient id="photo-shade" x1="0" y1="0" x2="0" y2="1">
          <stop offset="0" stop-color="var(--photo-dark)"/>
          <stop offset="0.7" stop-color="var(--photo-dark)" stop-opacity="0.85"/>
          <stop offset="1" stop-color="var(--photo-soft)" stop-opacity="0.5"/>
        </linearGradient>
      </defs>
      <polygon class="lane" points="240,75 390,140 520,1000 87,1000" fill="url(#lane-shade)" opacity="0.55"/>
      <g class="grid-lines" stroke="var(--grid-line)" stroke-width="2.6" fill="none">
        <polyline points="0,140 310,160 623,162"/>
        <line x1="0" y1="660" x2="623" y2="660"/>
        <line x1="307" y1="80" x2="307" y2="1000"/>
        <line x1="240" y1="75" x2="87" y2="1000"/>
        <line x1="385" y1="100" x2="520" y2="1000"/>
      </g>
      <rect class="photo-area" role="img" aria-label="Fotografie: kopfüber fallende Person in dunkler Kleidung"
            x="147" y="0" width="310" height="225" fill="url(#photo-shade)"/>
      <rect class="pen-photo" role="img" aria-label="Fotografie: senkrecht stehender schwarzer Füllfederhalter"
            x="300" y="815" width="16" height="185" fill="var(--photo-dark)"/>
    </svg>

    <div class="title-panel"></div>
    <h1 class="stacked-letters book-title" aria-label="Am Rande">
      <span>A</span><span>M</span><span>&nbsp;</span><span>R</span><span>A</span><span>N</span><span>D</span><span>E</span>
    </h1>
    <p class="stacked-letters author-name" aria-label="Lorenz Vadek">
      <span>L</span><span>O</span><span>R</span><span>E</span><span>N</span><span>Z</span><span>&nbsp;</span><span>V</span><span>A</span><span>D</span><span>E</span><span>K</span>
    </p>
    <p class="stacked-letters genre-label" aria-label="Roman">
      <span>R</span><span>O</span><span>M</span><span>A</span><span>N</span>
    </p>
  </div>
</body>
</html>
```